Wine Importer Needs a Wordpress Template

Our company, Corbusan Wine Merchants Ltd, requires a Wordpress template for our new website location (tarnelcask.ie).

We specialise in importing Moldovan wine into Ireland. I have attached a presentation that has background information about the main winery and its wine. I would very much like to see something similar to this in feel and colour. I have also attached our logo which might be useful.

We are very much open to new ideas, so long as the result is something that is clean and easy to use.

Many thanks.
Updates

Project Deadline Extended
Reason: I have extended the deadline by a few days given that I was unable to respond timely to queries. My apologies to all for this. I will be available from now until the new deadline.

Project Deadline Extended

Industry/Entity Type

It Company

```html
<!DOCTYPE html>
<html lang="en">
<head>
<meta charset="utf-8">
<title>Corbusan Wine Merchants Ltd</title>
<link href="https://fonts.googleapis.com/css2?family=Oswald:wght@300;400;500;700&family=Open+Sans:wght@400;600;700&family=Playfair+Display:ital,wght@0,400;0,700;1,400&display=swap" rel="stylesheet">
<style>
:root{
  --ink:#2b2925;
  --ink-deep:#1f1d1a;
  --hero:#3a3834;
  --green:#3f7d3b;
  --green-dark:#2f6430;
  --red:#b5272c;
  --paper:#f1eee6;
  --paper-dark:#e4dfd3;
  --muted:#8a857b;
  --light:#d8d3c8;
  --white:#ffffff;
}
*{box-sizing:border-box;margin:0;padding:0}
html,body{width:833px;height:1200px;overflow:hidden;background:var(--paper)}
body{font-family:"Open Sans",Arial,sans-serif;color:var(--ink);position:relative}
ul{list-style:none}

/* navigation */
.site-nav{height:60px;background:var(--ink-deep);display:flex;align-items:center;justify-content:center;gap:22px;position:relative;z-index:2}
.site-nav a{font-family:"Oswald",Arial,sans-serif;font-size:10px;letter-spacing:.8px;color:#cfcabf;text-decoration:none;text-transform:uppercase}
.site-nav a.active{background:var(--green);color:var(--white);padding:4px 9px}
.brand{display:flex;align-items:center;gap:7px;margin:0 26px}
.brand-dot{width:14px;height:14px;border-radius:50%;background:var(--green)}
.brand-name{font-family:"Oswald",Arial,sans-serif;font-size:13px;font-weight:500;color:var(--white);letter-spacing:1px}
.nav-cart{font-size:9px!important}

.sub-bar{height:22px;background:var(--paper-dark);font-size:8px;color:var(--muted);display:flex;align-items:center;padding-left:82px}
.sub-bar b{color:var(--ink);margin-left:4px}

/* hero */
.hero{height:298px;background:linear-gradient(180deg,#45423d 0%,var(--hero) 55%,#2c2a26 100%);position:relative;color:var(--white)}
.hero-bottles{position:absolute;left:92px;top:22px;width:215px;height:262px;background:linear-gradient(160deg,#e8e6e1 0%,#b9b4aa 45%,#4a2a2e 75%,#2a1d1f 100%);border-radius:2px}
.hero-copy{position:absolute;left:398px;top:68px;width:320px}
.hero-copy h1{font-family:"Oswald",Arial,sans-serif;font-weight:400;font-size:23px;line-height:1.12;letter-spacing:.5px;text-transform:uppercase}
.hero-copy p{font-size:9px;line-height:1.5;color:#d6d1c6;margin-top:9px;width:270px}
.btn{display:inline-block;font-family:"Oswald",Arial,sans-serif;font-size:10px;letter-spacing:.8px;color:var(--white);text-transform:uppercase;padding:6px 13px}
.btn-green{background:var(--green);margin-top:12px}
.btn-red{background:var(--red)}
.slide-arrow{position:absolute;top:140px;width:26px;height:26px;border-radius:50%;background:rgba(0,0,0,.45);display:flex;align-items:center;justify-content:center}
.slide-arrow.prev{left:96px}
.slide-arrow.next{right:96px}

/* vintage collection */
.collection{height:335px;background:linear-gradient(180deg,var(--paper) 0%,#e6e1d6 100%);text-align:center;padding-top:18px}
.section-title{font-family:"Playfair Display",Georgia,serif;font-size:22px;letter-spacing:1px}
.section-title .accent{color:var(--green)}
.section-title .plain{color:#7b776f}
.section-lead{font-size:8px;color:var(--muted);margin-top:3px}
.bottle-row{display:flex;justify-content:center;gap:14px;margin-top:22px}
.bottle-card{width:128px;height:250px;position:relative;padding-top:12px}
.bottle-card.featured{background:var(--white);box-shadow:0 3px 12px rgba(0,0,0,.18)}
.bottle{width:40px;height:180px;margin:0 auto;border-radius:14px 14px 4px 4px}
.bottle.red{background:linear-gradient(180deg,#1d1416 0%,#3b1f24 40%,#2a1a1c 100%)}
.bottle.rose{background:linear-gradient(180deg,#d9a1a6 0%,#e6b8ba 45%,#c98d93 100%)}
.bottle.white{background:linear-gradient(180deg,#9aa064 0%,#c7c98b 45%,#8f9456 100%)}
.bottle-tag{position:absolute;left:14px;right:14px;top:150px;background:var(--red)}
.bottle-name{font-size:8px;color:var(--ink);margin-top:12px;line-height:1.35}
.bottle-name span{display:block;color:var(--muted)}

/* story */
.story{height:305px;background:var(--ink);color:var(--white);text-align:center;padding-top:32px}
.story h2{font-family:"Oswald",Arial,sans-serif;font-weight:700;font-size:38px;line-height:1.05;text-transform:uppercase;letter-spacing:.5px}
.story-text{width:560px;margin:14px auto 0;font-size:8.5px;line-height:1.55;color:#cbc6bb}
.story-text b{color:var(--white)}
.stats{display:flex;align-items:flex-end;justify-content:center;gap:42px;margin-top:26px}
.stat strong{display:block;font-family:"Oswald",Arial,sans-serif;font-weight:300;font-size:46px;line-height:1;color:#6f6b63}
.stat small{display:block;font-size:8px;color:#aaa59b;text-align:left;margin-top:2px}
.stat-note{width:150px;font-size:8px;line-height:1.5;color:#aaa59b;text-align:left;padding-bottom:12px}

/* footer */
.site-footer{height:180px;background:var(--paper);padding:16px 82px 0}
.footer-cols{display:flex;justify-content:space-between}
.footer-col h3{font-family:"Playfair Display",Georgia,serif;font-style:italic;font-weight:700;font-size:13px;color:var(--green);margin-bottom:6px}
.footer-col li{font-size:8px;color:var(--muted);line-height:1.65}
.footer-col.contact{width:120px}
.footer-col.contact p{font-size:8px;color:var(--muted);line-height:1.5}
.footer-bottom{display:flex;justify-content:space-between;align-items:center;margin-top:14px;padding-top:8px;border-top:1px solid var(--light)}
.phones{display:flex;gap:16px;align-items:center;font-size:9px;font-weight:700;color:var(--ink)}
.phones span{display:flex;align-items:center;gap:5px}
.legal{display:flex;align-items:center;gap:12px;font-size:7.5px;color:var(--muted)}
</style>
</head>
<body>

<nav class="site-nav">
  <a class="active" href="#">Home</a>
  <a href="#">About our company</a>
  <a href="#">Products</a>
  <div class="brand"><span class="brand-dot"></span><span class="brand-name">CORBUSAN</span></div>
  <a href="#">How it works</a>
  <a href="#">Catalog</a>
  <a class="nav-cart" href="#">Cart (0)</a>
  <a href="#">Winemaking</a>
</nav>
<div class="sub-bar">Delivering to:<b>IRELAND</b></div>

<section class="hero">
  <div class="hero-bottles" role="img" aria-label="Gift box with bottles of vintage red wine"></div>
  <div class="slide-arrow prev"><svg width="10" height="10" viewBox="0 0 10 10"><path d="M6.5 1.5 3 5l3.5 3.5" stroke="#fff" stroke-width="1.6" fill="none"/></svg></div>
  <div class="slide-arrow next"><svg width="10" height="10" viewBox="0 0 10 10"><path d="M3.5 1.5 7 5 3.5 8.5" stroke="#fff" stroke-width="1.6" fill="none"/></svg></div>
  <div class="hero-copy">
    <h1>Wines maintain their<br>quality standards for<br>about 200 years.</h1>
    <p>There are few things in the world this constant. Even more so, at Château Lorvena perfection is the one thing that we bring to our customers. Since 1827.</p>
    <span class="btn btn-green">Order now &#9656;</span>
  </div>
</section>

<section class="collection">
  <h2 class="section-title"><span class="accent">VINTAGE</span> <span class="plain">COLLECTION</span></h2>
  <p class="section-lead">For more it is just good wine, but for us it is a song for the soul, it is art inherited from ancient times.</p>
  <div class="bottle-row">
    <div class="bottle-card">
      <div class="bottle red" role="img" aria-label="Bottle of dark red wine"></div>
      <p class="bottle-name">Negru de Lorvena 2014<span>Red dry wine</span></p>
    </div>
    <div class="bottle-card">
      <div class="bottle red" role="img" aria-label="Bottle of red wine"></div>
      <p class="bottle-name">Rosu de Lorvena 2013<span>Red dry wine</span></p>
    </div>
    <div class="bottle-card">
      <div class="bottle red" role="img" aria-label="Bottle of aged red wine"></div>
      <p class="bottle-name">Lorvena Reserve 1827<span>Red dry wine</span></p>
    </div>
    <div class="bottle-card featured">
      <div class="bottle rose" role="img" aria-label="Bottle of rosé wine"></div>
      <span class="btn btn-red bottle-tag">Order now</span>
      <p class="bottle-name">Roz de Lorvena 2015<span>Rosé dry wine</span></p>
    </div>
    <div class="bottle-card">
      <div class="bottle white" role="img" aria-label="Bottle of white wine"></div>
      <p class="bottle-name">Alb de Lorvena 2015<span>White dry wine</span></p>
    </div>
  </div>
</section>

<section class="story">
  <h2>Good wine,<br>a song for the soul...</h2>
  <p class="story-text">For most it is just good wine, but for us it is a song for the soul, it is art, inherited from ancient times. I am convinced that wine making is my vocation and I'm satisfied with the results I have achieved. For a long time I have had a dream: to create premium quality wines and develop a culture of proper wine consumption, structured around rich traditions &mdash; <b>the main purpose of life!</b></p>
  <div class="stats">
    <div class="stat"><strong>1827</strong><small>Founded</small></div>
    <div class="stat"><strong>250 h</strong><small>Of Vineyards</small></div>
    <div class="stat"><strong>1948</strong><small>&nbsp;</small></div>
    <p class="stat-note">The cellars of Château Lorvena contain an exclusive wine collection, some of bottles dating back to 1948.</p>
  </div>
</section>

<footer class="site-footer">
  <div class="footer-cols">
    <div class="footer-col"><h3>Browse Site</h3><ul><li>About Us</li><li>Our Wines</li><li>How It Works</li><li>Winemaking</li></ul></div>
    <div class="footer-col"><h3>What's New</h3><ul><li>Latest Offers</li><li>New Vintages</li><li>Wine Events</li><li>Gift Boxes</li></ul></div>
    <div class="footer-col"><h3>Delivery:</h3><ul><li>Delivery Areas</li><li>Delivery Costs</li><li>Returns Policy</li><li>Track Order</li></ul></div>
    <div class="footer-col"><h3>Shopping</h3><ul><li>My Account</li><li>Shopping Cart</li><li>Payment Options</li><li>FAQ</li></ul></div>
    <div class="footer-col contact"><h3>Contact Us</h3><p>Corbusan Wine Merchants Ltd<br>tarnelcask.ie</p></div>
  </div>
  <div class="footer-bottom">
    <div class="phones">
      <span><svg width="10" height="10" viewBox="0 0 10 10"><path d="M2 1h2l1 2.3-1.2.9a5.5 5.5 0 0 0 2 2L6.7 5 9 6v2c0 .6-.4 1-1 1C4.6 9 1 5.4 1 2c0-.6.4-1 1-1z" fill="#3f7d3b"/></svg>0800 418 2270</span>
      <span><svg width="10" height="10" viewBox="0 0 10 10"><path d="M2 1h2l1 2.3-1.2.9a5.5 5.5 0 0 0 2 2L6.7 5 9 6v2c0 .6-.4 1-1 1C4.6 9 1 5.4 1 2c0-.6.4-1 1-1z" fill="#3f7d3b"/></svg>+353 1 555 0142</span>
    </div>
    <div class="legal">
      <span>Copyright &copy; Corbusan Wine Merchants Ltd. All rights reserved.</span>
      <span class="btn btn-red">Order now &#9656;</span>
    </div>
  </div>
</footer>

</body>
</html>
```